Professional and creatice Life Coach - Business Card design

I just relaunched my website and now i a need a correspoonding business card for my task as life coach. My website is www.tbalrond.com as reference. The compass is kind of a symbol for my work, as I help people navigate through their challenging phases in life. The business card should be colorful, but not too playful as I also adress business people. So it sould be creative, but professional (also to suport my other business as Management Consultant)

Target Market(s)

People who want to get teir problems resolved, in business, partnership and other personal realms

Industry/Entity Type

Life Coaching

Contact Information for Business Card

Front side should include Name, Phone number, Email, Website and address

Font styles to use
Sans Serif

Colors
add136

Requirements
Must have
• "Mag. Leopold Brantner" -> Name
"Energetische Praxis" -> Jobtitle (describing my profession as life coach)
colours and style should match my website www.tbalrond.com
Nice to have
• a compass as a symbol

```html
<!DOCTYPE html>
<html lang="de">
<head>
<meta charset="utf-8">
<title>Leopold Brantner – Visitenkarte</title>
<link href="https://fonts.googleapis.com/css2?family=Lato:wght@400;700&display=swap" rel="stylesheet">
<style>
  :root {
    --brand-green: #add136;
    --brand-green-dark: #9cc02c;
    --card-white: #f6f8f2;
    --text-grey: #5a5c5e;
    --stage: #2b2e34;
    --white: #ffffff;
  }
  * { margin: 0; padding: 0; box-sizing: border-box; }
  html, body {
    width: 1200px; height: 900px; overflow: hidden;
    background: var(--stage);
    font-family: "Lato", sans-serif;
  }
  .canvas {
    position: relative; width: 1200px; height: 900px;
    display: flex; align-items: center; justify-content: center; gap: 60px;
  }
  .card {
    width: 520px; height: 320px; border-radius: 26px;
    position: relative; overflow: hidden;
    box-shadow: 0 18px 40px rgba(0,0,0,.35);
  }
  .card--front { background: var(--card-white); }
  .card--back {
    background: radial-gradient(circle at 50% 48%, rgba(255,255,255,.85) 0, rgba(255,255,255,.35) 70px, rgba(173,209,54,0) 160px), var(--brand-green);
    display: flex; align-items: center; justify-content: center;
  }
  .identity { position: absolute; left: 38px; top: 36px; }
  .identity__name {
    color: var(--brand-green); font-weight: 700; font-size: 21px;
    text-transform: uppercase; letter-spacing: .3px;
  }
  .identity__title {
    color: var(--text-grey); font-size: 12.5px; text-transform: uppercase;
    letter-spacing: .4px; margin-top: 3px;
  }
  .contact { position: absolute; left: 38px; top: 118px; list-style: none; }
  .contact__item {
    display: flex; align-items: center; gap: 10px;
    color: var(--text-grey); font-size: 14px; height: 30px;
  }
  .contact__icon {
    width: 21px; height: 21px; border-radius: 50%;
    background: var(--brand-green);
    display: flex; align-items: center; justify-content: center;
    flex: none;
  }
  .contact__icon svg { width: 12px; height: 12px; }
  .brand-mark {
    display: flex; align-items: center; gap: 10px;
    font-weight: 700;
  }
  .brand-mark__dot { border-radius: 50%; flex: none; }
  .card--front .brand-mark {
    position: absolute; right: 34px; bottom: 40px;
    color: var(--brand-green); font-size: 17px;
  }
  .card--front .brand-mark__dot { width: 26px; height: 26px; border: 3px solid var(--brand-green); }
  .card--back .brand-mark { color: var(--white); font-size: 26px; }
  .card--back .brand-mark__dot { width: 40px; height: 40px; border: 4px solid var(--white); }
</style>
</head>
<body>
<main class="canvas">
  <section class="card card--front" aria-label="Vorderseite">
    <header class="identity">
      <h1 class="identity__name">Mag. Leopold Brantner</h1>
      <p class="identity__title">Energetische Praxis</p>
    </header>
    <ul class="contact">
      <li class="contact__item">
        <span class="contact__icon"><svg viewBox="0 0 24 24" fill="#fff"><path d="M6.6 10.8a15.1 15.1 0 0 0 6.6 6.6l2.2-2.2a1 1 0 0 1 1-.25 11.4 11.4 0 0 0 3.6.57 1 1 0 0 1 1 1V20a1 1 0 0 1-1 1A17 17 0 0 1 3 4a1 1 0 0 1 1-1h3.5a1 1 0 0 1 1 1c0 1.250.2 2.45.57 3.57a1 1 0 0 1-.25 1z"/></svg></span>
        +43 664 3807152
      </li>
      <li class="contact__item">
        <span class="contact__icon"><svg viewBox="0 0 24 24" fill="none" stroke="#fff" stroke-width="2.4"><rect x="3" y="5" width="18" height="14" rx="1.5"/><path d="M3 6l9 7 9-7"/></svg></span>
        leopold@brantner.one
      </li>
      <li class="contact__item">
        <span class="contact__icon"><svg viewBox="0 0 24 24" fill="none" stroke="#fff" stroke-width="2.2"><circle cx="12" cy="12" r="9"/><path d="M3 12h18M12 3c3 3 3 15 0 18M12 3c-3 3-3 15 0 18"/></svg></span>
        www.tbalrond.com
      </li>
      <li class="contact__item">
        <span class="contact__icon"><svg viewBox="0 0 24 24" fill="#fff"><path d="M12 2a7 7 0 0 0-7 7c0 5 7 13 7 13s7-8 7-13a7 7 0 0 0-7-7zm0 9.5A2.5 2.5 0 1 1 12 6.5a2.5 2.5 0 0 1 0 5z"/></svg></span>
        Lindenweg 14, 6170 Bergstetten, Österreich
      </li>
    </ul>
    <div class="brand-mark"><span class="brand-mark__dot"></span>Leopold Brantner</div>
  </section>

  <section class="card card--back" aria-label="Rückseite">
    <div class="brand-mark"><span class="brand-mark__dot"></span>Leopold Brantner</div>
  </section>
</main>
</body>
</html>
```